Copper Kettle Catering
Business Cards and Letterhead
Copper Kettle Catering -
Creative Brief
Use standard fonts
R Danela Forsythe
Chef/Owner
287 W 93rd St FL2 New York, NY 10025
copperkettlecatering@mailbox.example
copperkettlecatering.example

```html
<!DOCTYPE html>
<html lang="en">
<head>
<meta charset="utf-8">
<title>Copper Kettle Catering – Business Cards</title>
<link rel="stylesheet" href="https://fonts.googleapis.com/css2?family=PT+Sans:wght@400;700&display=swap">
<style>
  :root {
    --bg: #ece7e1;
    --red: #e3212b;
    --gold: #e0a24c;
    --white: #ffffff;
    --ink: #3b3b3b;
    --brand: #c8161f;
  }
  * { box-sizing: border-box; margin: 0; padding: 0; }
  html, body { width: 1200px; height: 852px; overflow: hidden; }
  body {
    background: var(--bg);
    font-family: "PT Sans", Arial, sans-serif;
    position: relative;
  }
  .card {
    position: absolute;
    width: 520px;
    height: 320px;
    border-radius: 18px;
    overflow: hidden;
    box-shadow: 0 6px 18px rgba(0,0,0,0.18);
    background: var(--white);
  }
  .card--front { left: 90px; top: 80px; }
  .card--back  { left: 590px; top: 452px; }
  .card-shapes { position: absolute; inset: 0; }
  .brand-name {
    position: absolute;
    font-weight: 700;
    font-size: 26px;
    line-height: 1.1;
    color: var(--brand);
    text-align: center;
    width: 175px;
  }
  .card--front .brand-name { left: 338px; top: 112px; }
  .card--back .brand-name { left: 50px; top: 118px; }
  .holder-name { font-weight: 700; font-size: 18px; white-space: nowrap; }
  .holder-role { font-size: 11.5px; margin-top: 2px; }
  .address { font-size: 11.5px; line-height: 1.4; white-space: nowrap; }
  .contact-list { list-style: none; font-size: 10.5px; line-height: 1.6; }
  .contact-list li { display: flex; align-items: center; gap: 6px; white-space: nowrap; }
  .contact-list svg { width: 10px; height: 10px; flex: none; }

  .card--front .identity { position: absolute; left: 30px; top: 40px; color: var(--white); }
  .card--front .address { position: absolute; left: 30px; top: 138px; color: var(--white); }
  .card--front .contact-list { position: absolute; left: 30px; top: 212px; color: var(--white); }

  .card--back .identity { position: absolute; left: 282px; top: 52px; color: var(--ink); }
  .card--back .holder-name { color: var(--red); }
  .card--back .address { position: absolute; left: 282px; top: 104px; color: var(--ink); }
  .card--back .contact-list { position: absolute; right: 28px; top: 218px; color: var(--white); }
  .card--back .contact-list li { justify-content: flex-end; }
</style>
</head>
<body>

<section class="card card--front" aria-label="Business card front">
  <svg class="card-shapes" viewBox="0 0 520 320" preserveAspectRatio="none">
    <rect width="520" height="320" fill="var(--red)"/>
    <path d="M318 0 C 308 110 288 230 258 320 L 270 320 C 300 230 320 110 330 0 Z" fill="var(--gold)"/>
    <path d="M330 0 L520 0 L520 320 L270 320 C 300 230 320 110 330 0 Z" fill="var(--white)"/>
  </svg>
  <div class="brand-name">Copper Kettle Catering</div>
  <div class="identity">
    <div class="holder-name">R Danela Forsythe</div>
    <div class="holder-role">Chef/Owner</div>
  </div>
  <div class="address">287 W 93rd St FL2<br>New York, NY 10025</div>
  <ul class="contact-list">
    <li><svg viewBox="0 0 12 12"><path d="M3 1 L5 3.5 L4 5 C4.8 6.6 5.6 7.4 7 8 L8.5 7 L11 9 L9.5 11 C5 10.5 1.5 7 1 2.5 Z" fill="currentColor"/></svg>555.014.7720</li>
    <li><svg viewBox="0 0 12 12"><rect x="3" y="1" width="6" height="10" rx="1" fill="currentColor"/></svg>555.018.3391</li>
    <li><svg viewBox="0 0 12 12"><circle cx="6" cy="6" r="5" fill="none" stroke="currentColor" stroke-width="1.5"/><circle cx="6" cy="6" r="2" fill="currentColor"/></svg>copperkettlecatering@mailbox.example</li>
    <li><svg viewBox="0 0 12 12"><circle cx="6" cy="6" r="5" fill="none" stroke="currentColor" stroke-width="1.5"/><path d="M1 6 H11 M6 1 V11" stroke="currentColor" stroke-width="1"/></svg>copperkettlecatering.example</li>
  </ul>
</section>

<section class="card card--back" aria-label="Business card back">
  <svg class="card-shapes" viewBox="0 0 520 320" preserveAspectRatio="none">
    <rect width="520" height="320" fill="var(--white)"/>
    <path d="M520 28 C 436 140 294 236 156 320 L 170 320 C 300 240 440 150 520 40 Z" fill="var(--gold)"/>
    <path d="M520 40 C 440 150 300 240 170 320 L520 320 Z" fill="var(--red)"/>
  </svg>
  <div class="brand-name">Copper Kettle Catering</div>
  <div class="identity">
    <div class="holder-name">R Danela Forsythe</div>
    <div class="holder-role">Chef/Owner</div>
  </div>
  <div class="address">287 W 93rd St FL2<br>New York, NY 10025</div>
  <ul class="contact-list">
    <li>555.014.7720<svg viewBox="0 0 12 12"><path d="M3 1 L5 3.5 L4 5 C4.8 6.6 5.6 7.4 7 8 L8.5 7 L11 9 L9.5 11 C5 10.5 1.5 7 1 2.5 Z" fill="currentColor"/></svg></li>
    <li>555.018.3391<svg viewBox="0 0 12 12"><rect x="3" y="1" width="6" height="10" rx="1" fill="currentColor"/></svg></li>
    <li>copperkettlecatering@mailbox.example<svg viewBox="0 0 12 12"><circle cx="6" cy="6" r="5" fill="none" stroke="currentColor" stroke-width="1.5"/><circle cx="6" cy="6" r="2" fill="currentColor"/></svg></li>
    <li>copperkettlecatering.example<svg viewBox="0 0 12 12"><circle cx="6" cy="6" r="5" fill="none" stroke="currentColor" stroke-width="1.5"/><path d="M1 6 H11 M6 1 V11" stroke="currentColor" stroke-width="1"/></svg></li>
  </ul>
</section>

</body>
</html>
```